Gobal construction supply company needs new business card design

I need a business card design for my global supply company using an existing logo. i will be looking to print these on rounded corner cards with the black background version of my logo on the back. on the front white background, my logo again and my simple details.

```html
<!DOCTYPE html>
<html lang="en">
<head>
<meta charset="utf-8">
<title>Coastline Industrial Supply – Business Card</title>
<link href="https://fonts.googleapis.com/css2?family=Open+Sans:wght@400;600;700&display=swap" rel="stylesheet">
<style>
  :root {
    --backdrop: #2b2b2b;
    --card-black: #141414;
    --card-white: #ffffff;
    --ink: #1b1b1b;
    --band: #1e1c20;
    --accent: #d81e1e;
  }
  * { margin: 0; padding: 0; box-sizing: border-box; }
  html, body { width: 1200px; height: 900px; overflow: hidden; }
  body {
    background: var(--backdrop);
    font-family: "Open Sans", Arial, sans-serif;
    position: relative;
  }
  .card {
    position: absolute;
    left: 250px;
    width: 700px;
    height: 400px;
    border-radius: 28px;
    overflow: hidden;
  }
  .card-back { top: 40px; background: var(--card-black); color: var(--card-white); }
  .card-front { top: 460px; background: var(--card-white); color: var(--ink); }

  .brand-name {
    position: absolute;
    font-weight: 700;
    letter-spacing: 0.5px;
    line-height: 1.2;
  }
  .card-back .brand-name {
    left: 0; right: 0; top: 140px;
    text-align: center;
    font-size: 27px;
    color: var(--card-white);
  }
  .card-front .brand-name {
    right: 40px; top: 66px;
    text-align: right;
    font-size: 23px;
    color: var(--ink);
  }

  .website {
    position: absolute; left: 0; right: 0; top: 318px;
    text-align: center; font-size: 17px; color: var(--card-white);
  }
  .website .domain { color: var(--accent); }

  .front-bands { position: absolute; left: 0; top: 0; width: 700px; height: 400px; }

  .person { position: absolute; left: 58px; top: 190px; }
  .person-name { font-weight: 700; font-size: 22px; letter-spacing: 0.5px; }
  .person-role { color: var(--accent); font-size: 15px; font-weight: 600; margin-top: 1px; }
  .contact-list { list-style: none; margin-top: 10px; }
  .contact-list li {
    display: flex; align-items: center; gap: 8px;
    font-size: 15.5px; line-height: 25px;
  }
  .contact-icon { width: 16px; height: 16px; flex: none; }

  .address {
    position: absolute; left: 58px; bottom: 20px;
    color: var(--card-white); font-size: 16px;
  }
</style>
</head>
<body>

<section class="card card-back" aria-label="Card back">
  <div class="brand-name">COASTLINE INDUSTRIAL<br>SUPPLY</div>
  <p class="website">www.<span class="domain">coastlinesupply</span>.com.au</p>
</section>

<section class="card card-front" aria-label="Card front">
  <svg class="front-bands" viewBox="0 0 700 400" aria-hidden="true">
    <polygon points="480,336 518,282 700,282 700,336" fill="var(--accent)"/>
    <rect x="0" y="336" width="700" height="64" fill="var(--band)"/>
  </svg>

  <div class="brand-name">COASTLINE INDUSTRIAL<br>SUPPLY</div>

  <div class="person">
    <div class="person-name">DANIEL HARROW</div>
    <div class="person-role">MANAGING DIRECTOR</div>
    <ul class="contact-list">
      <li>
        <svg class="contact-icon" viewBox="0 0 16 16" aria-hidden="true">
          <circle cx="8" cy="8" r="8" fill="var(--accent)"/>
          <path d="M4 7.5c0-1.8 1.8-3 4-3s4 1.2 4 3l-1.6.4-.4-1.2H6l-.4 1.2z M5.5 9h5v2.5h-5z" fill="#fff"/>
        </svg>
        555 210 44 80
      </li>
      <li>
        <svg class="contact-icon" viewBox="0 0 16 16" aria-hidden="true">
          <circle cx="8" cy="8" r="8" fill="var(--accent)"/>
          <rect x="5.5" y="3.5" width="5" height="9" rx="1" fill="#fff"/>
          <rect x="6.5" y="4.8" width="3" height="5.5" fill="var(--accent)"/>
        </svg>
        888 730 16 52
      </li>
      <li>
        <svg class="contact-icon" viewBox="0 0 16 16" aria-hidden="true">
          <circle cx="8" cy="8" r="8" fill="var(--accent)"/>
          <rect x="4" y="5" width="8" height="6" fill="#fff"/>
          <path d="M4 5l4 3.3L12 5" fill="none" stroke="var(--accent)" stroke-width="1"/>
        </svg>
        d.harrow@coastlinesupply.com.au
      </li>
    </ul>
  </div>

  <p class="address">48 Harbour Road, Eastfield, New York 12401</p>
</section>

</body>
</html>
```